Business card design needed

We are a Custom Joinery and specialise in design, Manufacture and Installation of kitchens and cabinetry
We currently have a logo based on the northern star in red and black but are open to something that would look fresh and clean
Updates

Project Deadline Extended
Reason: Need a couple days to go through designs. Finding some designs that are great on front and others great on reverse. I would like to be able to comment and get the total look we are after.

Target Market(s)

30-50 year olds who are looking to renovate

Industry/Entity Type

Business

Contact Information for Business Card

Larchfield Fitouts
ABN 37 418 260 573
Colin Pratley - Cabinetmaker/Designer Licence No. 318570K

Requirements
Nice to have
• Maybe a nice fresh modern kitchen picture

```html
<!DOCTYPE html>
<html lang="en">
<head>
<meta charset="utf-8">
<title>Larchfield Fitouts – Business Card</title>
<link href="https://fonts.googleapis.com/css2?family=Signika:wght@400;600&display=swap" rel="stylesheet">
<style>
  :root {
    --page-bg: #e9eaec;
    --card-bg: #ffffff;
    --brand-red: #d0161b;
    --ink: #2b2b2b;
    --ink-soft: #4a4a4a;
    --logo-grey: #55555a;
    --kitchen-light: #e4e1dc;
    --kitchen-mid: #9c958d;
    --kitchen-dark: #3b3632;
  }
  * { box-sizing: border-box; margin: 0; padding: 0; }
  html, body {
    width: 1200px;
    height: 861px;
    overflow: hidden;
    background: var(--page-bg);
    font-family: "Signika", Arial, sans-serif;
  }
  .card {
    position: absolute;
    left: 410px;
    top: 95px;
    width: 380px;
    height: 640px;
    background: var(--card-bg);
    overflow: hidden;
    box-shadow: 0 10px 30px rgba(0,0,0,0.18);
  }
  .card__kitchen {
    position: absolute;
    left: 0; right: 0; bottom: 0;
    height: 370px;
    background: linear-gradient(to bottom,
      rgba(255,255,255,1) 0%,
      var(--kitchen-light) 30%,
      var(--kitchen-mid) 62%,
      var(--kitchen-dark) 100%);
  }
  .card__content { position: relative; padding: 0 40px; }
  .brand {
    display: flex;
    align-items: center;
    gap: 12px;
    margin-top: 62px;
    justify-content: center;
  }
  .brand__mark {
    width: 22px; height: 22px;
    background: var(--brand-red);
  }
  .brand__name {
    font-size: 28px;
    font-weight: 400;
    color: var(--logo-grey);
    letter-spacing: 0.5px;
  }
  .person { margin-top: 80px; }
  .person__name {
    font-size: 37px;
    font-weight: 600;
    color: var(--brand-red);
    line-height: 1;
  }
  .person__role {
    font-size: 20px;
    color: var(--ink);
    margin-top: 6px;
  }
  .contacts { margin-top: 30px; list-style: none; }
  .contact {
    display: flex;
    align-items: flex-start;
    gap: 12px;
    font-size: 14px;
    color: var(--ink-soft);
    line-height: 1.45;
    margin-bottom: 6px;
  }
  .contact__icon { flex: none; width: 18px; height: 18px; margin-top: 1px; }
  .credentials { margin-top: 4px; font-size: 14px; color: var(--ink-soft); }
  .credential { margin-bottom: 7px; }
  .credential__label { color: var(--brand-red); font-weight: 600; }
</style>
</head>
<body>
  <article class="card">
    <div class="card__kitchen" role="img" aria-label="Photo of a bright modern white kitchen with cabinetry, benchtop and bar stools"></div>

    <div class="card__content">
      <header class="brand">
        <span class="brand__mark"></span>
        <span class="brand__name">Larchfield Fitouts</span>
      </header>

      <section class="person">
        <h1 class="person__name">Colin Pratley</h1>
        <p class="person__role">Cabinetmaker/Designer</p>
      </section>

      <ul class="contacts">
        <li class="contact">
          <svg class="contact__icon" viewBox="0 0 18 18" aria-hidden="true">
            <circle cx="9" cy="9" r="9" fill="var(--brand-red)"/>
            <rect x="5.5" y="4.5" width="7" height="9" fill="#fff"/>
            <rect x="7" y="6" width="1.5" height="1.5" fill="var(--brand-red)"/>
            <rect x="9.5" y="6" width="1.5" height="1.5" fill="var(--brand-red)"/>
            <rect x="7" y="8.5" width="1.5" height="1.5" fill="var(--brand-red)"/>
            <rect x="9.5" y="8.5" width="1.5" height="1.5" fill="var(--brand-red)"/>
            <rect x="8.2" y="11" width="1.6" height="2.5" fill="var(--brand-red)"/>
          </svg>
          <span>Unit 12, 8-14 Calder St<br>Kingsford NSW 2032</span>
        </li>
        <li class="contact">
          <svg class="contact__icon" viewBox="0 0 18 18" aria-hidden="true">
            <circle cx="9" cy="9" r="9" fill="var(--brand-red)"/>
            <rect x="5.5" y="6" width="7" height="7" rx="1.2" fill="#fff"/>
            <rect x="6.5" y="4.5" width="5" height="2" rx="1" fill="#fff"/>
            <circle cx="9" cy="9.5" r="1.6" fill="var(--brand-red)"/>
          </svg>
          <span>9360 2284</span>
        </li>
        <li class="contact">
          <svg class="contact__icon" viewBox="0 0 18 18" aria-hidden="true">
            <circle cx="9" cy="9" r="9" fill="var(--brand-red)"/>
            <rect x="7.5" y="3.5" width="3.5" height="11" rx="1" fill="#fff" transform="rotate(35 9 9)"/>
          </svg>
          <span>0412 556 093</span>
        </li>
        <li class="contact">
          <svg class="contact__icon" viewBox="0 0 18 18" aria-hidden="true">
            <circle cx="9" cy="9" r="9" fill="var(--brand-red)"/>
            <rect x="4.5" y="5.8" width="9" height="6.4" fill="#fff"/>
            <path d="M4.5 5.8 L9 9.6 L13.5 5.8" fill="none" stroke="var(--brand-red)" stroke-width="1"/>
          </svg>
          <span>larchfieldfitouts@mail.com.au</span>
        </li>
      </ul>

      <div class="credentials">
        <p class="credential"><span class="credential__label">Licence No.</span> 318570K</p>
        <p class="credential"><span class="credential__label">ABN</span> 37 418 260 573</p>
      </div>
    </div>
  </article>
</body>
</html>
```